Commercial Refrigeration Service Company requires stylish and fresh looking flyer.

We need a flyer to hand out to new customers. It should have a photo and our branding, list all the services that are offered and our contact details.
We would like two flyers to be supplied, both identical though one offering a discount until July ( Half Price Service Fee ). The flyer should be clear, interesting and in similar colours to the branding package supplied.
Please look at our website for information about the services on offer:
www.frostvale-cooling.com.au

Target Market(s)

Cafes, bars, restaurants, pubs ect.

Font styles to use
Other font styles liked:
• Font package provided

Colors
85cae6
ffffff
333333

Requirements
Must have
• - The photo provided.
• - The company logo.
• - Similar feel to the website & business card.
• - Smooth layout and clear to understand.
Should not have
• - No clunky badges or prints.

```html
<!DOCTYPE html>
<html lang="en">
<head>
<meta charset="utf-8">
<title>Frostvale Commercial Refrigeration Flyer</title>
<link rel="stylesheet" href="https://fonts.googleapis.com/css2?family=Montserrat:wght@400;500&family=Oswald:wght@500&family=Open+Sans:wght@700&family=Roboto+Condensed:wght@400&display=swap">
<style>
  :root {
    --brand-blue: #5ac2ea;
    --label-blue: #55bce6;
    --ink: #333333;
    --paper-top: #f6f6f6;
    --paper-bottom: #e3e3e3;
    --stage: #4a4a4a;
    --white: #ffffff;
  }
  * { margin: 0; padding: 0; box-sizing: border-box; }
  html, body { width: 1200px; height: 1146px; overflow: hidden; }
  body { background: var(--stage); position: relative; }

  .flyer {
    position: absolute; left: 224px; top: 40px;
    width: 753px; height: 1066px;
    background: linear-gradient(var(--paper-top), var(--paper-bottom));
    overflow: hidden;
  }
  .photo {
    position: absolute; left: 0; top: 0; width: 753px; height: 300px;
    background: linear-gradient(180deg, #9cc3df 0%, #c9d6de 38%, #7d858d 62%, #5c6066 100%);
  }
  .brand-band {
    position: absolute; left: 0; top: 300px; width: 753px; height: 152px;
    background: var(--brand-blue);
    display: flex; align-items: center; justify-content: center;
  }
  .brand-name {
    font-family: 'Montserrat', sans-serif; font-weight: 500;
    font-size: 46px; letter-spacing: 0.04em;
    color: var(--ink);
  }
  .tagline {
    position: absolute; left: 0; top: 480px; width: 753px; text-align: center;
    font-family: 'Montserrat', sans-serif; font-weight: 500;
    font-size: 22px; letter-spacing: 0.04em; color: var(--ink);
  }

  .services-title {
    position: absolute; top: 558px; left: 0; width: 753px; text-align: center;
    font-family: 'Open Sans', sans-serif; font-weight: 700; font-size: 19px; color: var(--ink);
  }
  .service-diagram { position: absolute; left: 0; top: 0; }
  .service-label {
    position: absolute; font-family: 'Oswald', sans-serif; font-weight: 500;
    font-size: 18px; line-height: 21px; color: var(--label-blue); letter-spacing: -0.01em;
  }
  .align-right { text-align: right; }

  .contact {
    position: absolute; top: 963px; left: 0; width: 753px; text-align: center;
    font-family: 'Roboto Condensed', sans-serif; font-size: 15.5px; line-height: 20px; color: var(--ink);
  }
  .footer {
    position: absolute; left: 0; top: 1020px; width: 753px; height: 46px; background: var(--ink);
  }
  .web-address {
    position: absolute; left: 0; width: 730px; top: 9px; text-align: center;
    font-family: 'Montserrat', sans-serif; font-weight: 500; font-size: 21px;
    letter-spacing: 0.09em; color: var(--brand-blue);
  }
  .social-dots { position: absolute; right: 20px; top: 12px; display: flex; gap: 4px; }
  .social-dots span { width: 21px; height: 21px; border-radius: 50%; background: var(--white); }
</style>
</head>
<body>
  <div class="flyer">
    <div class="photo" role="img" aria-label="Photo of the technician leaning on the branded service ute at a beachside car park"></div>

    <div class="brand-band"><span class="brand-name">Frostvale</span></div>

    <p class="tagline">Commercial Refrigeration</p>

    <h2 class="services-title">OUR SERVICES</h2>

    <svg class="service-diagram" width="753" height="1066" viewBox="0 0 753 1066">
      <g fill="#7b7b7b" stroke="#5ac2ea" stroke-width="2">
        <rect x="241" y="597" width="46" height="46" transform="rotate(45 264 620)"/>
        <rect x="461" y="605" width="46" height="46" transform="rotate(45 484 628)"/>
        <rect x="212" y="703" width="46" height="46" transform="rotate(45 235 726)"/>
        <rect x="493" y="705" width="46" height="46" transform="rotate(45 516 728)"/>
        <rect x="250" y="806" width="46" height="46" transform="rotate(45 273 829)"/>
        <rect x="353" y="839" width="46" height="46" transform="rotate(45 376 862)"/>
        <rect x="465" y="817" width="46" height="46" transform="rotate(45 488 840)"/>
      </g>
      <g fill="none" stroke="#ffffff" stroke-width="1.6" stroke-linecap="round" stroke-linejoin="round">
        <path d="M262 603 v22 a5 5 0 1 0 4 0 v-22 a2 2 0 0 0 -4 0 z M270 607 h4 M270 612 h4 M270 617 h4"/>
        <path d="M472 639 l20 -20 l4 4 l-20 20 h-4 z M476 614 l20 20 l-4 4 l-20 -20 z"/>
        <path d="M226 714 h18 l-2 24 h-14 z M230 722 h5 v5 h-5 z M236 729 h5 v5 h-5 z"/>
        <path d="M502 720 h5 l3 12 h15 l3 -9 h-19 M512 737 a1.5 1.5 0 1 0 0.1 0 M524 737 a1.5 1.5 0 1 0 0.1 0"/>
        <path d="M265 822 h12 v8 h-4 v-4 h-8 z M271 815 v7 M273 833 v6"/>
        <path d="M380 848 l-9 15 h7 l-4 13 l10 -17 h-7 l5 -11 z"/>
        <path d="M478 830 l20 20 M498 830 l-20 20 M475 827 l5 0 l0 5 M501 853 a3 3 0 1 0 0.1 0"/>
      </g>
    </svg>

    <p class="service-label align-right" style="right:532px; top:582px;">COMMERCIAL<br>REFRIGERATION</p>
    <p class="service-label" style="left:516px; top:592px;">INSTALLATION</p>
    <p class="service-label align-right" style="right:563px; top:716px;">ICE MAKERS</p>
    <p class="service-label" style="left:562px; top:717px;">SALES</p>
    <p class="service-label align-right" style="right:517px; top:839px;">BEER SYSTEMS</p>
    <p class="service-label" style="left:341px; top:907px;">ELECTRICAL</p>
    <p class="service-label" style="left:519px; top:857px;">24HR SERVICE</p>

    <p class="contact">PO Box 4471 Bayview NSW 2104 | 0412 555 018<br>info@frostvale-cooling.com.au | ABN: 12 345 678 901 | Licence No: 418273D</p>

    <div class="footer">
      <p class="web-address">WWW.FROSTVALE-COOLING.COM.AU</p>
      <div class="social-dots"><span></span><span></span><span></span></div>
    </div>
  </div>
</body>
</html>
```